Brennock Holdings LLC, new Business cards

I'm moving offices and need new cards. Plus I'm open to modifying the current design of my card. I will keep the logo but would like to explore other layouts and fonts for the design. I've included the current double sided card for reference. I Like the navy color and white. Might be open to grays or silver. Needs to be clean and elegant.

Target Market(s)

Investors, buyers & sellers of private equities and real estate.

Contact Information for Business Card

Brennock Holdings
Desmond K.R. Whitfield, Managing Principal
418 Harwick Ave., Suite 310
Denver, CO 80299
M: 970-555-0147, O: 303-555-0193
Desmond@brennockholdings.example
Brennockholdings.example

Colors
0354a2
ffffff
c4c4c4

Requirements
Must have
• Business card details.
• Logo raised or embossed, it was designed after a wax seal. Current has raised ink.
Nice to have
• Space on card to write additional notes.

```html
<!DOCTYPE html>
<html lang="en">
<head>
<meta charset="utf-8">
<title>Brennock Holdings — Business Card</title>
<link href="https://fonts.googleapis.com/css2?family=Montserrat:wght@400;500;600;700&display=swap" rel="stylesheet">
<style>
  :root {
    --backdrop: #3a3a3c;
    --navy: #2d2a5e;
    --card-white: #ececec;
    --card-gray-top: #7a7a7a;
    --card-gray-bottom: #5f5f5f;
    --ink: #2d2a5e;
    --rule: #2d2a5e;
  }
  * { margin: 0; padding: 0; box-sizing: border-box; }
  html, body {
    width: 1200px;
    height: 1000px;
    overflow: hidden;
    background: var(--backdrop);
    font-family: "Montserrat", sans-serif;
  }
  .sheet {
    position: relative;
    width: 1200px;
    height: 1000px;
  }
  .card {
    position: absolute;
    left: 220px;
    width: 760px;
    height: 420px;
    border-radius: 28px;
    box-shadow: 0 12px 30px rgba(0,0,0,0.35);
  }
  .card--front {
    top: 50px;
    background: linear-gradient(160deg, var(--card-gray-top), var(--card-gray-bottom));
    display: flex;
    align-items: center;
    justify-content: center;
  }
  .card--back {
    top: 520px;
    background: var(--card-white);
  }
  .brand {
    display: flex;
    align-items: center;
    gap: 14px;
    color: var(--navy);
    font-weight: 600;
    font-size: 26px;
    letter-spacing: 0.04em;
  }
  .brand__dot {
    width: 22px;
    height: 22px;
    border-radius: 50%;
    background: var(--navy);
    flex: none;
  }
  .card--back .brand {
    position: absolute;
    left: 60px;
    top: 188px;
  }
  .details {
    position: absolute;
    right: 60px;
    top: 110px;
    text-align: right;
    color: var(--ink);
  }
  .details__name {
    font-size: 22px;
    font-weight: 600;
  }
  .details__title {
    font-size: 13px;
    font-weight: 500;
    margin-top: 4px;
  }
  .details__rule {
    width: 92px;
    height: 2px;
    background: var(--rule);
    margin: 22px 0 22px auto;
  }
  .details__company {
    font-size: 16px;
    font-weight: 700;
  }
  .details__line {
    font-size: 15px;
    font-weight: 500;
    line-height: 1.3;
  }
  .contact {
    margin-top: 4px;
    list-style: none;
  }
  .contact__item {
    display: flex;
    justify-content: flex-end;
    align-items: center;
    gap: 8px;
    font-size: 15px;
    font-weight: 500;
    line-height: 1.35;
  }
  .contact__icon {
    width: 13px;
    height: 13px;
    flex: none;
  }
</style>
</head>
<body>
<main class="sheet">
  <section class="card card--front" aria-label="Card front">
    <div class="brand"><span class="brand__dot"></span>Brennock Holdings</div>
  </section>

  <section class="card card--back" aria-label="Card back">
    <div class="brand"><span class="brand__dot"></span>Brennock Holdings</div>

    <div class="details">
      <p class="details__name">Desmond K.R. Whitfield</p>
      <p class="details__title">Managing Principal</p>
      <div class="details__rule"></div>
      <p class="details__company">Brennock Holdings</p>
      <p class="details__line">418 Harwick Ave., Suite 310</p>
      <p class="details__line">Denver, CO 80299</p>
      <ul class="contact">
        <li class="contact__item">970-555-0147, O: TBD
          <svg class="contact__icon" viewBox="0 0 16 16" aria-hidden="true"><path fill="#2d2a5e" d="M3.6 1.5l2.3 2.4-1.2 1.8c.9 2 2.4 3.6 4.5 4.6l1.8-1.2 2.5 2.3-1.3 2.1C7.6 13.8 2.2 8.4 1.7 3z"/></svg>
        </li>
        <li class="contact__item">desmond@brennockholdings.example
          <svg class="contact__icon" viewBox="0 0 16 16" aria-hidden="true"><rect x="1" y="3" width="14" height="10" rx="1.5" fill="#2d2a5e"/><path d="M2 4.5l6 4.5 6-4.5" fill="none" stroke="#ececec" stroke-width="1.3"/></svg>
        </li>
        <li class="contact__item">www.brennockholdings.example
          <svg class="contact__icon" viewBox="0 0 16 16" aria-hidden="true"><circle cx="8" cy="8" r="7" fill="#2d2a5e"/><g fill="none" stroke="#ececec" stroke-width="1"><ellipse cx="8" cy="8" rx="3" ry="7"/><path d="M1 8h14M2.5 4.5h11M2.5 11.5h11"/></g></svg>
        </li>
      </ul>
    </div>
  </section>
</main>
</body>
</html>
```